Law Firm Website

I currently have a temporary site that I created myself at www.mcorveyfirm.net (hosted by 9tree). I am generally happy with the content.

My permanent website just has basic information right now: www.mcorveyfirm.com (hosted by lumenrack). I want to take the general content from the temporary website and have a more professional looking website on the permanent website. I want it in Wordpress format. I want a link to my blog: www.crookedpath.com. I want it to work on pads and smart phones. My number and e-mail address should be available on every page. The idea is to feature the potential client more than the lawyer.
Updates

Several of the designs are good. I would like the front page to have my number and address at the top (and at the top of every page) and to identify my law firm as "Law Office of Gerald T. Corvey". No need to include "mcorveyfirm" as that is just the web address. I like showing the most recent blog posts on the front page. I don't need video. No need to emphasize office hours or map location on the front page (that could be under a contact button). My picture should be somewhere. I would like an image from Boston on the front page if we can find one that is not copyright protected. No images of gavels or scales of justice. See some of the sample websites I listed in previous messages. Thanks!

Industry/Entity Type

Law Firm

```html
<!DOCTYPE html>
<html lang="en">
<head>
<meta charset="utf-8">
<title>Law Office of Gerald T. Corvey – Attorney of Law</title>
<link rel="stylesheet" href="https://fonts.googleapis.com/css2?family=Arimo:wght@400;700&family=Libre+Baskerville:wght@400;700&family=Playfair+Display:ital,wght@1,700&display=swap">
<style>
:root{
  --dark:#2b2d2b;
  --beige:#d6d2ca;
  --tan-light:#f3ece1;
  --tan:#c9b69a;
  --blue:#3b84c8;
  --blue-dark:#2862a0;
  --blue-deep:#1f4f85;
  --navy:#173a5e;
  --ink:#1d1d1d;
  --grey:#8a8a8a;
  --text:#333;
  --white:#fff;
  --link:#3a86c9;
}
*{box-sizing:border-box;margin:0;padding:0}
html,body{width:908px;height:1200px;overflow:hidden}
body{position:relative;background:var(--beige);font-family:"Arimo",Arial,sans-serif;color:var(--text)}
.abs{position:absolute}

.top-band{left:0;top:0;width:908px;height:56px;background:linear-gradient(90deg,var(--tan) 0%,var(--tan-light) 18%,var(--tan-light) 82%,var(--tan) 100%)}
.dark-band{left:0;top:99px;width:908px;height:218px;background:var(--dark)}
.brand{left:66px;top:8px;width:320px;text-align:center}
.brand-name{font-family:"Libre Baskerville",Georgia,serif;font-weight:700;font-size:17px;color:var(--ink);line-height:22px;padding-bottom:3px;border-bottom:2px solid var(--ink);display:inline-block}
.brand-tag{font-family:"Arimo",Arial,sans-serif;font-size:11px;color:var(--ink);margin-top:3px}
.phone{left:524px;top:15px;display:flex;align-items:center;gap:8px;font-family:"Arimo",Arial,sans-serif;font-weight:700;font-size:23px;line-height:26px;color:#3b3b3b}
.avatar{left:738px;top:10px;width:38px;height:38px;border-radius:50%;background:linear-gradient(#6b7a8c,#3a4657);border:2px solid #fff}

.hero{left:123px;top:56px;width:663px;height:236px;background:linear-gradient(120deg,#9aa6b4 0%,#d8dde3 40%,#eef1f4 55%,#7d8ea3 100%)}
.hero-caption{left:123px;top:208px;width:663px;height:67px;background:rgba(40,40,40,.55);padding:6px 10px;color:var(--white)}
.hero-caption h2{font-family:"Libre Baskerville",Georgia,serif;font-weight:400;font-size:18px;margin-bottom:6px}
.hero-caption p{font-size:9.5px;line-height:13px}

.main-nav{left:123px;top:292px;width:663px;height:33px;background:linear-gradient(#4a94d6,var(--blue-dark));display:flex;align-items:center}
.main-nav a{color:var(--white);text-decoration:none;font-size:12px;height:33px;line-height:33px;text-align:center;border-right:1px solid rgba(255,255,255,.3)}
.main-nav a:last-child{border-right:0}

.features{left:123px;top:328px;width:663px;height:127px;background:linear-gradient(#5b9bd1,var(--blue-dark));display:flex}
.feature{flex:1;text-align:center;color:var(--white);padding-top:14px}
.feature svg{display:block;margin:0 auto;height:42px}
.feature h3{font-weight:400;font-size:15px;margin-top:6px}
.feature .btn{display:inline-block;margin-top:10px;width:64px;height:22px;line-height:22px;background:var(--navy);border-radius:3px;font-size:9px;color:var(--white)}

.content-bg{left:123px;top:455px;width:663px;height:644px;background:#eeeeec}
.content-card{left:124px;top:474px;width:431px;height:620px;background:var(--white);border-radius:0 22px 22px 22px;box-shadow:0 3px 8px rgba(0,0,0,.25)}
.profile{left:134px;top:487px;width:410px;height:177px;border:1px solid #ddd;background:var(--white)}
.profile-photo{left:151px;top:515px;width:69px;height:67px;background:linear-gradient(#8895a5,#3f4b5c);border:3px solid #e2e2e2}
.profile-name{left:260px;top:530px;font-size:22px;color:var(--ink)}
.profile-sub{left:268px;top:559px;font-size:10px;color:var(--grey)}
.profile-info{left:147px;top:595px;font-size:10px;line-height:12.5px;color:var(--grey)}

.welcome{left:142px;top:689px;font-size:14px;font-weight:400;color:var(--ink)}
.welcome span{color:var(--link)}
.intro{left:150px;top:713px;width:390px;font-size:8.6px;line-height:11.4px;color:#222}
.intro p{text-indent:20px;margin-bottom:11px}

.news{left:134px;top:932px;width:410px;height:120px;border:1px solid #ddd}
.news h4{position:absolute;left:17px;top:8px;font-family:"Libre Baskerville",Georgia,serif;font-weight:400;font-size:12px;color:var(--link)}
.news-item{position:absolute;top:30px;width:180px;font-size:8.5px;line-height:11px}
.news-item b{display:block;color:var(--ink)}
.news-item .date{color:#444;margin-bottom:10px}
.news-item p{color:#555}

.areas-title{left:572px;top:484px;width:198px;text-align:center;font-family:"Playfair Display",Georgia,serif;font-style:italic;font-weight:700;font-size:15px;color:var(--ink)}
.areas{left:582px;top:513px;width:180px;list-style:none}
.areas li{height:28px;margin-bottom:4.5px;background:linear-gradient(90deg,#f6efe4,#c9b497);border:1px solid #a89477;display:flex;align-items:center;justify-content:space-between;padding:0 6px 0 8px;font-size:11px;color:var(--ink);white-space:nowrap}
.areas li svg{width:14px;height:14px;flex:none}

.contact-form{left:580px;top:873px;width:180px;height:214px;background:linear-gradient(#4c8fcf,var(--blue-deep));border:2px solid #8ab6e2}
.contact-form h3{font-family:"Libre Baskerville",Georgia,serif;font-size:12px;color:var(--white);text-align:center;margin-top:12px}
.field{position:absolute;left:12px;font-size:9px;color:var(--white)}
.field-box{position:absolute;left:56px;width:106px;height:18px;background:var(--white)}
.send{position:absolute;right:22px;bottom:14px;font-size:9px;color:var(--white)}

.footer{left:0;top:1099px;width:908px;height:101px;background:var(--dark)}
.footer-nav{left:0;top:1119px;width:908px;display:flex;justify-content:center;gap:36px;font-size:10px;color:var(--white)}
.follow{left:0;top:1140px;width:908px;text-align:center;font-size:7.5px;color:var(--white)}
.social{left:421px;top:1159px;display:flex;gap:4px}
.social span{width:15px;height:15px;background:#5d8fc2}
.copyright{left:0;top:1183px;width:908px;height:17px;background:#1a1b1a;text-align:center;font-size:7.5px;line-height:17px;color:var(--white)}
</style>
</head>
<body>
<div class="abs top-band"></div>
<div class="abs dark-band"></div>

<header>
  <div class="abs brand">
    <div class="brand-name">Law Office of Gerald T. Corvey</div>
    <div class="brand-tag">Attorney of Law</div>
  </div>
  <div class="abs phone">
    <svg width="20" height="24" viewBox="0 0 20 24"><path d="M5 2c2 0 3 5 2 6-1 1-2 1-1 4s3 5 5 6c2 0 2-1 3-1s4 3 3 5c-1 2-4 2-6 1C5 20 1 12 2 6c0-3 1-4 3-4z" fill="#b5232a"/></svg>
    <span>(617) 555 - 0142</span>
  </div>
  <div class="abs avatar" role="img" aria-label="Portrait of the attorney"></div>
</header>

<section class="abs hero" role="img" aria-label="Photo of smiling business people in a meeting"></section>
<div class="abs hero-caption">
  <h2>Lorem Ipsum Dolor Sit Amet</h2>
  <p>Lorem ipsum dolor sit amet, consectetur adipiscing elit sed diem nonumy in convalis gravida neque. Nulla gravida vestibulum metis a acumsan, aliquam in sagitis ut. Solicitudin sed massa ud enim veniam. Curabitur tempus sem vitae mi vestibulum volutpat malesuada.</p>
</div>

<nav class="abs main-nav">
  <a href="#" style="width:86px">HOME</a>
  <a href="#" style="width:124px">ATTORNEY PROFILE</a>
  <a href="#" style="width:124px">PRACTICE AREA</a>
  <a href="#" style="width:76px">BLOG</a>
  <a href="#" style="width:76px">NEWS</a>
  <a href="#" style="width:117px">CONTACT US</a>
</nav>

<section class="abs features">
  <div class="feature">
    <svg viewBox="0 0 56 42" width="56"><ellipse cx="30" cy="16" rx="20" ry="13" fill="#e8eef5"/><path d="M18 26l-6 12 14-9z" fill="#e8eef5"/></svg>
    <h3>TESTIMONIALS</h3>
    <span class="btn">Click Here</span>
  </div>
  <div class="feature">
    <svg viewBox="0 0 56 42" width="56"><rect x="14" y="4" width="28" height="34" rx="3" fill="#e8eef5"/><rect x="19" y="11" width="18" height="3" fill="#2862a0"/><rect x="19" y="18" width="18" height="3" fill="#2862a0"/><rect x="19" y="25" width="12" height="3" fill="#2862a0"/></svg>
    <h3>LATEST BLOG POSTS</h3>
    <span class="btn">Click Here</span>
  </div>
  <div class="feature">
    <svg viewBox="0 0 56 42" width="56"><circle cx="28" cy="21" r="17" fill="none" stroke="#e8eef5" stroke-width="4"/><text x="28" y="25" text-anchor="middle" font-family="Arimo, Arial, sans-serif" font-weight="700" font-size="13" fill="#fff">24</text></svg>
    <h3>FREE CONSULTATION</h3>
    <span class="btn">Click Here</span>
  </div>
</section>

<div class="abs content-bg"></div>
<main>
  <div class="abs content-card"></div>
  <div class="abs profile"></div>
  <div class="abs profile-photo" role="img" aria-label="Portrait of Gerald T. Corvey"></div>
  <div class="abs profile-name">Gerald T. Corvey</div>
  <div class="abs profile-sub">Law Office of Gerald T. Corvey</div>
  <div class="abs profile-info">
    48, Harlow St. 4th floor<br>
    Boston, MA 021 0 9 - 3318<br>
    (617) 555 0142<br>
    email &nbsp;&nbsp;: gcorvey@mcorveyfirm.com<br>
    Blog &nbsp;&nbsp;&nbsp;: www.crookedpath.com
  </div>

  <h1 class="abs welcome">Welcome to the <span>Law Office of Gerald T. Corvey</span></h1>
  <div class="abs intro">
    <p>Lorem ipsum dolor sit amet, consectetur adipiscing elit. set diem nonumy in convalis gravida neque. Nulla gravida vestibulum metis a acumsan, aliquam in sagitis ut. Solicitudin sed massa ud enim veniam. Curabitur tempus sem vitae mi vestibulum volutpat malesu ada erat vestibulum. Sed aliquam dolor at dolor conse quat gravida. Fusce mineque tempus nec fequat sit amet. Tincidunt ut lec. Nam semper omare enim.</p>
    <p>Lorem ipsum dolor sit amet, consectetur adipiscing elit. set diem nonumy inconvalis gravida neque. Nulla gravida vestibulum metis a acumsan, aliquam in sagitis ut. Solicitudin sed massa ud enim veniam. Curabitur tempus sem vitae mi vestibulum volutpat malesu ada erat vestibulum. Sed aliallwuam dolor at dolor consequat gravida. Fusce mineque tempus neq fequat sit amet. Tincidunt ut leo. Nam semper omare enim.</p>
    <p>Lorem ipsum dolor sit amet., consectetur adipiscing elit. set diem nonumy in convalis gravida neque. Nulla gravida vestibulum metis a acumsan, aliquam in sagitis ut. Solicitudin sed massa ud nim veniam. Curabitur tempus em vitae mi vestibulum volutpat malesuada erat vestibulum. set aliquam dolor at dolor consequat gravida. fusce mineque nec fequat sit amet. Tincidunt ut leo. Nam semper omare enim.</p>
  </div>

  <section class="abs news">
    <h4>Latest News</h4>
    <div class="news-item" style="left:17px">
      <b>Lorem Ipsum Dolor Sit Amet, Consectetuer Adipiscing Elit.</b>
      <div class="date">Friday, may 9. 2014</div>
      <p>Lorem ipsum dolor sit amet, consectetuer adipiscing elit. Sed diem nonumy in convalis gravida...</p>
    </div>
    <div class="news-item" style="left:216px">
      <b>Lorem Ipsum Dolor Sit Amet, Consectetuer Adipiscing Elit.</b>
      <div class="date">Monday, June 17, 2014</div>
      <p>Lorem ipsum dolor sit amet, consectetuer adipiscing elit. Sed diem nonumy in convalis gravida...</p>
    </div>
  </section>

  <aside>
    <h2 class="abs areas-title">Areas Of Practice</h2>
    <ul class="abs areas">
      <li>Criminal Defense<svg viewBox="0 0 14 14"><circle cx="7" cy="7" r="6.5" fill="#3b84c8"/><path d="M5.5 4l4 3-4 3z" fill="#fff"/></svg></li>
      <li>Criminal Law Info<svg viewBox="0 0 14 14"><circle cx="7" cy="7" r="6.5" fill="#3b84c8"/><path d="M5.5 4l4 3-4 3z" fill="#fff"/></svg></li>
      <li>Type of Crimes<svg viewBox="0 0 14 14"><circle cx="7" cy="7" r="6.5" fill="#3b84c8"/><path d="M5.5 4l4 3-4 3z" fill="#fff"/></svg></li>
      <li>Driving under The influence<svg viewBox="0 0 14 14"><circle cx="7" cy="7" r="6.5" fill="#3b84c8"/><path d="M5.5 4l4 3-4 3z" fill="#fff"/></svg></li>
      <li>Drug Crimes<svg viewBox="0 0 14 14"><circle cx="7" cy="7" r="6.5" fill="#3b84c8"/><path d="M5.5 4l4 3-4 3z" fill="#fff"/></svg></li>
      <li>Juvenile Crimes<svg viewBox="0 0 14 14"><circle cx="7" cy="7" r="6.5" fill="#3b84c8"/><path d="M5.5 4l4 3-4 3z" fill="#fff"/></svg></li>
      <li>Sex Crimes<svg viewBox="0 0 14 14"><circle cx="7" cy="7" r="6.5" fill="#3b84c8"/><path d="M5.5 4l4 3-4 3z" fill="#fff"/></svg></li>
      <li>Theft Crimes<svg viewBox="0 0 14 14"><circle cx="7" cy="7" r="6.5" fill="#3b84c8"/><path d="M5.5 4l4 3-4 3z" fill="#fff"/></svg></li>
      <li>Violent Crimes<svg viewBox="0 0 14 14"><circle cx="7" cy="7" r="6.5" fill="#3b84c8"/><path d="M5.5 4l4 3-4 3z" fill="#fff"/></svg></li>
      <li>White Collar Crimes<svg viewBox="0 0 14 14"><circle cx="7" cy="7" r="6.5" fill="#3b84c8"/><path d="M5.5 4l4 3-4 3z" fill="#fff"/></svg></li>
    </ul>

    <form class="abs contact-form">
      <h3>Tell Me About Your Case</h3>
      <label class="field" style="top:57px">Name</label><span class="field-box" style="top:53px"></span>
      <label class="field" style="top:82px">Email</label><span class="field-box" style="top:78px"></span>
      <label class="field" style="top:107px">Phone</label><span class="field-box" style="top:103px"></span>
      <label class="field" style="top:132px">Message</label><span class="field-box" style="top:128px;height:50px"></span>
      <span class="send">Send Your Message</span>
    </form>
  </aside>
</main>

<footer>
  <div class="abs footer"></div>
  <div class="abs footer-nav"><span>HOME</span><span>ATTORNEY PROFILE</span><span>PRACTICE AREA</span><span>BLOG</span><span>NEWS</span><span>CONTACT US</span></div>
  <div class="abs follow">FOLLOW US ON :</div>
  <div class="abs social"><span></span><span></span><span></span><span></span></div>
  <div class="abs copyright">Company © 2014, Law Office of Gerald T. Corvey. All rights reserved.</div>
</footer>
</body>
</html>
```